Real Estate Website - Phase I

We are looking to re-design our company website completely.
This will be for a real estate company which focuses on multiple lines of business/customers, including

1) Buyers - Investors, Owner Occupants
2) Sellers - Short Sales, Limited Services/Flat Fee, and Corporate/REO clients (the last being our core current customer)
3) Other Services: Default Services, Institutional Property Management, Field and Inspection Services
4) Agent FAQ's, instructions, etc to tie into our web-based offer management systems

For a brief understanding of what we do - Please see www.tvlomar.com. Current site does not address all of our current services.

Website must be able to be edited/added onto over time. We are also looking at redirects so that certain pages/sections can be given unique domain names to drive core customers to.

We work both with normal agents and buyers and large scale financial institutions, therefore our focus must be specific to each unique group based on the applicable page(s).

We had an incorrect amount in this brief.  It has since been corrected.

Please re-review.

Industry/Entity Type

Real Estate

Requirements
Must have
• *Property Search/Display - By various criteria AND by map
*Property Management back end for putting in new properties
*MObile Version or Mobile Friendly
*Analytics
*Contact Management and Lead Capture functions, including ability to export or use from site for email marketing campaigns. Lead capture must be able to sort by various criteria to tailor campaigns, ability to send out auto notices to staff and those signing up, etc.
* Signup option w/ functions for viewing not yet on market properties (subscription). This needs to be able to let buyers set search criteria and be auto notified whenever a property was listed or adjusted that met their criteria.
* SEO Optimization
* Syndication options to allow ease of syndication
* FAQ's and assistance pages to agents working with us
* Blog, social media boxes
* Ability for buyers to submit initial offers direct
* Functions and pages specific to below, with ability to cross promote and track (inquiry forms, etc to the below)
*Dedicated or preferred lender(s)
* Preferred vendors, etc

```html
<!DOCTYPE html>
<html lang="en">
<head>
<meta charset="utf-8">
<title>Tvlomar Realty – Home</title>
<link href="https://fonts.googleapis.com/css2?family=Source+Sans+3:wght@400;600;700&display=swap" rel="stylesheet">
<style>
:root{
  --ink:#333333;
  --muted:#555555;
  --accent:#1a9ad6;
  --navy:#2b2f7a;
  --hero:#e08a72;
  --rule:#6d6d6d;
  --panel-head:#6a6a6a;
  --field:#ffffff;
  --field-border:#c9c9c9;
  --btn:#2f5a8f;
  --footer:#3a3a3a;
  --footer-deep:#0d0d0d;
  --link:#3d8fd0;
  --white:#ffffff;
}
*{box-sizing:border-box;margin:0;padding:0}
html,body{width:1200px;height:1000px;overflow:hidden;background:var(--white)}
body{position:relative;font-family:"Source Sans 3",Arial,sans-serif;color:var(--ink)}
.abs{position:absolute}

/* header */
.brand{left:348px;top:12px;display:flex;align-items:center;gap:6px}
.brand-mark{width:32px;height:34px;background:var(--navy)}
.brand-name{font-size:17px;font-weight:600;color:var(--navy);letter-spacing:.2px}
.contact-block{left:790px;top:9px;font-size:7.5px;line-height:12px;color:var(--ink)}
.header-rule{left:288px;top:60px;width:624px;height:2px;background:var(--rule)}
.main-nav{left:347px;top:62px;height:24px;display:flex;font-size:10px}
.main-nav a{color:var(--ink);text-decoration:none;padding:0 4px;line-height:24px}
.main-nav a.active{background:#000;color:var(--white);padding:0 5px}

/* hero */
.hero{left:288px;top:87px;width:624px;height:296px;background:var(--hero)}
.hero-photo{left:350px;top:110px;width:351px;height:239px;border:2px solid #f1f1f1;
  background:linear-gradient(180deg,#cfd8dc 0%,#9fa98a 35%,#d8cdb4 55%,#4e6a3a 85%,#6d7a55 100%)}
.search-panel{left:700px;top:110px;width:150px;height:239px;
  background:linear-gradient(180deg,#fbfbfb 0%,#eeeeee 100%);box-shadow:0 2px 4px rgba(0,0,0,.25)}
.search-head{height:24px;background:var(--panel-head);color:var(--white);font-size:9px;
  font-weight:700;letter-spacing:1px;text-align:center;line-height:24px}
.toggle-row{position:absolute;left:9px;top:40px;width:132px;display:flex;justify-content:space-between;
  align-items:center;font-size:8px;color:var(--muted)}
.select{position:absolute;height:17px;background:var(--field);border:1px solid var(--field-border);
  font-size:7.5px;color:#777;line-height:15px;padding-left:5px}
.select::after{content:"";position:absolute;right:0;top:0;width:17px;height:15px;
  background:linear-gradient(#d5d5d5,#a9a9a9)}
.select svg{position:absolute;right:4px;top:5px;z-index:1}
.search-btn{position:absolute;left:78px;top:198px;width:63px;height:18px;border-radius:2px;
  background:linear-gradient(#4a78ad,var(--btn));color:var(--white);font-size:8px;font-weight:600;
  text-align:center;line-height:18px}
.adv-link{position:absolute;right:9px;top:224px;font-size:7.5px;color:var(--muted)}

/* proposals */
.section-title{left:348px;top:395px;font-size:19px;color:var(--accent);font-weight:400;text-transform:uppercase}
.card{position:absolute;top:428px;width:120px}
.card-photo{width:116px;height:77px;border:3px solid #dcdcdc}
.card h3{font-size:12.5px;font-weight:400;color:var(--accent);margin-top:5px;white-space:nowrap}
.card p{font-size:7px;line-height:11.5px;color:var(--ink)}
.btn-details{display:inline-block;margin-top:7px;background:var(--accent);color:var(--white);
  font-size:6.5px;padding:2px 6px}

/* services */
.service{position:absolute;top:604px;width:118px}
.service h4{font-size:12.5px;font-weight:400;color:var(--accent);margin-bottom:8px}
.service p,.service li{font-size:6.6px;line-height:10.2px;color:var(--muted)}
.service p+p{margin-top:6px}
.service ul{list-style:none}
.service ul.plain li{margin-bottom:5px}
.service ol{list-style:none}
.service ol li{margin-bottom:5px;padding-left:7px;text-indent:-7px}
.read-more{display:block;text-align:right;font-size:6.5px;color:var(--accent);margin-top:6px}

/* footer */
.footer{left:288px;top:767px;width:624px;height:196px;background:var(--footer);color:var(--white)}
.footer h5{position:absolute;top:15px;font-size:10px;font-weight:700}
.agents{position:absolute;left:60px;top:42px;display:grid;grid-template-columns:repeat(3,47px);gap:7px 3px}
.agent-photo{width:47px;height:38px;border:2px solid #e0e0e0;background:linear-gradient(#f4f4f4,#cfcfcf)}
.tweets{position:absolute;left:233px;top:38px;width:150px;font-size:6.8px;line-height:12.5px}
.tweets .tweet{margin-bottom:3px}
.tweets a,.tweets .when{color:var(--link);text-decoration:none}
.contact-form{position:absolute;left:408px;top:41px;width:155px;font-size:6.8px}
.field-row{display:flex;align-items:center;margin-bottom:5px}
.field-row label{width:26px;padding-left:3px}
.field-row span{display:block;width:128px;height:14px;background:#000}
.message{width:155px;height:64px;background:#000;margin-top:1px}
.send-btn{margin:8px 0 0 110px;width:45px;height:13px;background:var(--white);color:var(--ink);
  text-align:center;line-height:13px;font-size:7px}
.bottom-bar{left:288px;top:963px;width:624px;height:37px;background:var(--footer-deep)}
.copyright{position:absolute;left:59px;top:15px;font-size:6.5px;color:#bbb}
.social{position:absolute;left:483px;top:10px;display:flex;gap:4px}
.social span{width:17px;height:17px;border-radius:50%;background:#8a8a8a}
</style>
</head>
<body>

<header>
  <div class="abs brand">
    <div class="brand-mark"></div>
    <div class="brand-name">Tvlomar Realty</div>
  </div>
  <address class="abs contact-block" style="font-style:normal">
    Tvlomar Realty<br>Main:555-014-2270<br>Fax:555-014-2291<br>info@tvlomar.com
  </address>
  <div class="abs header-rule"></div>
  <nav class="abs main-nav">
    <a class="active" href="#">Home</a><a href="#">About</a><a href="#">Buying</a><a href="#">Selling</a><a href="#">Blog</a><a href="#">FAQ's</a><a href="#">Functions</a>
  </nav>
</header>

<section class="abs hero"></section>
<div class="abs hero-photo" role="img" aria-label="Photo of a two-storey family house with a covered porch among trees"></div>

<form class="abs search-panel">
  <div class="search-head">QUICK SEARCH</div>
  <div class="toggle-row">
    <span>For Sale</span>
    <svg width="36" height="10" viewBox="0 0 36 10"><rect x="2" y="3" width="32" height="4" rx="2" fill="#777"/><circle cx="8" cy="5" r="4.5" fill="#e2e2e2" stroke="#999"/></svg>
    <span>For Rent</span>
  </div>
  <div class="select" style="left:9px;top:64px;width:132px">Location<svg width="8" height="5"><path d="M0 0h8L4 5z" fill="#fff"/></svg></div>
  <div class="select" style="left:9px;top:90px;width:132px">Property type<svg width="8" height="5"><path d="M0 0h8L4 5z" fill="#fff"/></svg></div>
  <div class="select" style="left:9px;top:116px;width:132px">Square Feet<svg width="8" height="5"><path d="M0 0h8L4 5z" fill="#fff"/></svg></div>
  <div class="select" style="left:9px;top:143px;width:64px">Beds<svg width="8" height="5"><path d="M0 0h8L4 5z" fill="#fff"/></svg></div>
  <div class="select" style="left:77px;top:143px;width:64px">Baths<svg width="8" height="5"><path d="M0 0h8L4 5z" fill="#fff"/></svg></div>
  <div class="select" style="left:9px;top:169px;width:64px">Min price<svg width="8" height="5"><path d="M0 0h8L4 5z" fill="#fff"/></svg></div>
  <div class="select" style="left:77px;top:169px;width:64px">Max price<svg width="8" height="5"><path d="M0 0h8L4 5z" fill="#fff"/></svg></div>
  <div class="search-btn">Search</div>
  <div class="adv-link">Advanced Search</div>
</form>

<h2 class="abs section-title">Best Proposala</h2>

<article class="card" style="left:348px">
  <div class="card-photo" role="img" aria-label="Modern white apartment building with a pool" style="background:linear-gradient(#5d8fd0 0%,#b8c9e0 40%,#e8e8e8 65%,#4aa3c7 100%)"></div>
  <h3>Lorem ipsum dolor</h3>
  <p>&nbsp;sit amet,consectetur adi<br>pisicing elit, sed do eiusmod tempor<br>&nbsp;Ut enim ad minim</p>
  <span class="btn-details">Details</span>
</article>
<article class="card" style="left:478px">
  <div class="card-photo" role="img" aria-label="White villa with red tiled roof" style="background:linear-gradient(#c9dbe8 0%,#d9683f 35%,#f2efe9 60%,#9ab07a 100%)"></div>
  <h3>Lorem ipsum dolor</h3>
  <p>&nbsp;sit amet,consectetur adi<br>pisicing elit, sed do eiusmod tempor<br>&nbsp;Ut enim ad minim</p>
  <span class="btn-details">Details</span>
</article>
<article class="card" style="left:606px">
  <div class="card-photo" role="img" aria-label="Row of suburban houses along a street" style="background:linear-gradient(#b9cce0 0%,#8a9aa8 40%,#d9d9d4 65%,#7fa35c 100%)"></div>
  <h3>Lorem ipsum dolor</h3>
  <p>&nbsp;sit amet,consectetur adi<br>pisicing elit, sed do eiusmod tempor<br>&nbsp;Ut enim ad minim</p>
  <span class="btn-details">Details</span>
</article>
<article class="card" style="left:734px">
  <div class="card-photo" role="img" aria-label="Brick house on a lawn with a for sale sign" style="background:linear-gradient(#4d86c9 0%,#9a7a55 40%,#b99562 60%,#5f8a34 100%)"></div>
  <h3>Lorem ipsum dolor</h3>
  <p>&nbsp;sit amet,consectetur adi<br>pisicing elit, sed do eiusmod tempor<br>&nbsp;Ut enim ad minim</p>
  <span class="btn-details">Details</span>
</article>

<section class="service" style="left:349px">
  <h4>Buyers</h4>
  <p>If you are interested in purchasing an available property or obtaining further information, click on For Buyers.</p>
  <p>You can also access up-to-date infor-mation and request a showing on all of our area listings at the touch of a button by visiting our Current Listings page.</p>
  <span class="read-more">Read more &gt;&gt;</span>
</section>
<section class="service" style="left:479px">
  <h4>Sellers</h4>
  <p>We now offer specialized seller services including Short Sale and Limited Services options to sellers, in addition to traditional listing services. Learn more about our Seller Services here.</p>
  <span class="read-more">Read more &gt;&gt;</span>
</section>
<section class="service" style="left:605px;width:125px">
  <h4>Other Services</h4>
  <ul class="plain">
    <li>Default Services</li>
    <li>Institutional Property Management</li>
    <li>Field and Inspection Services</li>
  </ul>
</section>
<section class="service" style="left:734px">
  <h4>Agent FAQ's</h4>
  <ol>
    <li>1) Lorem ipsum dolor sit amet ?<br>&nbsp;&nbsp;&nbsp;&nbsp;consectetur adipisicing elit.</li>
    <li>2) Lorem ipsum dolor sit amet ?<br>&nbsp;&nbsp;&nbsp;&nbsp;consectetur adipisicing elit.</li>
    <li>3) Lorem ipsum dolor sit amet ?<br>&nbsp;&nbsp;&nbsp;&nbsp;consectetur adipisicing elit.</li>
  </ol>
</section>

<footer class="abs footer">
  <h5 style="left:59px">Our Agents</h5>
  <div class="agents">
    <div class="agent-photo" role="img" aria-label="Agent portrait"></div>
    <div class="agent-photo" role="img" aria-label="Agent portrait"></div>
    <div class="agent-photo" role="img" aria-label="Agent portrait"></div>
    <div class="agent-photo" role="img" aria-label="Agent portrait"></div>
    <div class="agent-photo" role="img" aria-label="Agent portrait"></div>
    <div class="agent-photo" role="img" aria-label="Agent portrait"></div>
  </div>

  <h5 style="left:234px">Last Tweets</h5>
  <div class="tweets">
    <div class="tweet">Lorem ipsum dolor sit amet <a href="#">@stranger</a> labore ut enim ad ullamco <a href="#">http://lipsum #dolorsit amet</a><br><span class="when">4 day ago</span></div>
    <div class="tweet">&nbsp;Lorem ipsum <a href="#">@stranger</a> labore utenim ad &nbsp;ullamco.<br><span class="when">&nbsp;4 day ago</span></div>
    <div class="tweet">Lorem ipsum dolor sit amet <a href="#">@stranger</a> labore ut enim ad ullamco <a href="#">http://lipsum #dolorsit amet</a><br><span class="when">4 day ago</span></div>
  </div>

  <h5 style="left:408px">Contact us</h5>
  <div class="contact-form">
    <div class="field-row"><label>Name</label><span></span></div>
    <div class="field-row"><label>Email</label><span></span></div>
    <div class="message"></div>
    <div class="send-btn">Send</div>
  </div>
</footer>

<div class="abs bottom-bar">
  <p class="copyright">Copyright © 2013 Tvlomar Companies. All rights reserved.</p>
  <div class="social" aria-label="Social links"><span></span><span></span><span></span><span></span></div>
</div>

</body>
</html>
```